Business card for STEADYWAVE

Please design professional business card for IT consulting firm STEADYWAVE INC.
Use logo attached.
Use information from sample qNode business card attached.
replace qnode inc with STEADYWAVE INC.
as well as qnodeinc.com with steadywave.example

```html
<!DOCTYPE html>
<html lang="en">
<head>
<meta charset="UTF-8">
<title>STEADYWAVE Business Card</title>
<link href="https://fonts.googleapis.com/css2?family=Montserrat:wght@400;500;600;700&display=swap" rel="stylesheet">
<style>
  :root {
    --bg: #1b1b1d;
    --card: #232325;
    --card-edge: #2b2b2e;
    --ink: #ffffff;
    --ink-soft: #e6e6e8;
    --gloss: #3a3a3d;
    --accent: #9b1fe8;
  }
  * { margin: 0; padding: 0; box-sizing: border-box; }
  html, body {
    width: 1200px; height: 900px; overflow: hidden;
    background: var(--bg);
    font-family: "Montserrat", sans-serif;
  }
  .stage {
    position: relative; width: 1200px; height: 900px;
    display: flex; flex-direction: column; align-items: center; justify-content: center; gap: 34px;
  }
  .card {
    position: relative; width: 700px; height: 400px;
    background: var(--card);
    border: 1px solid var(--card-edge);
    box-shadow: 0 18px 40px rgba(0,0,0,0.45);
  }
  .card-front { display: flex; align-items: center; justify-content: center; }
  .wordmark {
    display: flex; align-items: center; gap: 14px;
    font-weight: 700; letter-spacing: 0.1em; text-transform: uppercase;
  }
  .card-front .wordmark { font-size: 50px; color: var(--gloss); }
  .wordmark-mark { width: 22px; height: 22px; background: currentColor; }
  .card-back .wordmark { font-size: 38px; color: var(--ink); }
  .card-back .wordmark-mark { width: 16px; height: 16px; background: var(--accent); }
  .card-back { display: flex; align-items: center; padding-left: 46px; }
  .card-back .wordmark { width: 360px; }
  .divider {
    width: 2px; height: 210px; background: var(--accent); margin: 0 30px 0 22px;
  }
  .contact { color: var(--ink-soft); }
  .contact-name {
    font-size: 23px; font-weight: 600; color: var(--accent); letter-spacing: 0.02em; line-height: 1.1;
  }
  .contact-role { font-size: 16px; font-weight: 500; color: var(--ink); margin-bottom: 14px; letter-spacing: 0.03em; }
  .contact-address { font-size: 16px; line-height: 1.4; font-style: normal; margin-bottom: 10px; }
  .contact-list { list-style: none; font-size: 16px; line-height: 1.55; }
  .contact-list li { display: flex; align-items: center; gap: 9px; }
  .contact-list svg { width: 12px; height: 12px; flex: none; }
</style>
</head>
<body>
<main class="stage">
  <section class="card card-front" aria-label="Card front">
    <div class="wordmark">STEADYWAVE<span class="wordmark-mark"></span></div>
  </section>

  <section class="card card-back" aria-label="Card back">
    <div class="wordmark">STEADYWAVE<span class="wordmark-mark"></span></div>
    <div class="divider"></div>
    <div class="contact">
      <p class="contact-name">DANIEL MORROW</p>
      <p class="contact-role">DIRECTOR</p>
      <address class="contact-address">5120 Harbourline Court,<br>Suite 204, Northvale,<br>ON, Canada, Ontario</address>
      <ul class="contact-list">
        <li>
          <svg viewBox="0 0 12 12" aria-hidden="true"><path d="M2.5 1h2l1 2.5-1.3 1a6 6 0 0 0 3.3 3.3l1-1.3L11 7.5v2A1.5 1.5 0 0 1 9.5 11 8.5 8.5 0 0 1 1 2.5 1.5 1.5 0 0 1 2.5 1z" fill="none" stroke="#9b1fe8" stroke-width="1.1"/></svg>
          +1 555-014-2290
        </li>
        <li>
          <svg viewBox="0 0 12 12" aria-hidden="true"><rect x="1" y="2.5" width="10" height="7" fill="none" stroke="#9b1fe8" stroke-width="1.1"/><path d="M1 2.5l5 4 5-4" fill="none" stroke="#9b1fe8" stroke-width="1.1"/></svg>
          info@steadywave.example
        </li>
        <li>
          <svg viewBox="0 0 12 12" aria-hidden="true"><circle cx="6" cy="6" r="5" fill="none" stroke="#9b1fe8" stroke-width="1.1"/><ellipse cx="6" cy="6" rx="2.2" ry="5" fill="none" stroke="#9b1fe8" stroke-width="1"/><path d="M1 6h10" stroke="#9b1fe8" stroke-width="1"/></svg>
          www.steadywave.example
        </li>
      </ul>
    </div>
  </section>
</main>
</body>
</html>
```